Corvana Wound Care Business card design

We need a business card designed around our logo which was provided. The logo of preference is the colored. Also the colors and fonts were provided.

Target Market(s)

Our Referral partners are home health agencies.

Industry/Entity Type

Healthcare

Contact Information for Business Card

Name , Phone #, Email , Title

Requirements
Nice to have
• Creativity
Should not have
• basic

```html
<!DOCTYPE html>
<html lang="en">
<head>
<meta charset="utf-8">
<title>Corvana Wound Care – Business Card</title>
<link href="https://fonts.googleapis.com/css2?family=Montserrat:wght@500;600&family=Tinos&display=swap" rel="stylesheet">
<style>
  :root {
    --backdrop: #3a3b3e;
    --card: #070708;
    --brand-blue: #1565b8;
    --name-blue: #1f8fe0;
    --icon-blue: #2a6fd0;
    --text-light: #f2f2f2;
    --rule: #d9d9d9;
  }
  * { margin: 0; padding: 0; box-sizing: border-box; }
  html, body { width: 1200px; height: 915px; overflow: hidden; }
  body {
    background: var(--backdrop);
    position: relative;
    font-family: "Montserrat", sans-serif;
  }
  .card {
    position: absolute;
    left: 250px;
    width: 700px;
    height: 400px;
    background: var(--card);
    border-radius: 34px;
  }
  .card--front { top: 35px; }
  .card--back { top: 480px; }

  .brand {
    position: absolute;
    display: flex;
    align-items: center;
    gap: 16px;
  }
  .brand__dot {
    width: 34px; height: 34px;
    border-radius: 50%;
    background: var(--brand-blue);
    flex: none;
  }
  .brand__name {
    font-weight: 600;
    color: var(--brand-blue);
    white-space: nowrap;
  }
  .card--front .brand { left: 50%; top: 50%; transform: translate(-50%, -50%); }
  .card--front .brand__name { font-size: 40px; }
  .card--back .brand { right: 80px; top: 62px; }
  .card--back .brand__dot { width: 30px; height: 30px; }
  .card--back .brand__name { font-size: 34px; }

  .person {
    position: absolute;
    left: 110px; top: 170px;
  }
  .person__name {
    font-size: 25px;
    font-weight: 500;
    color: var(--name-blue);
    line-height: 1.1;
    white-space: nowrap;
  }
  .person__title {
    font-size: 19px;
    font-weight: 500;
    color: var(--text-light);
    margin-top: 8px;
  }
  .address {
    position: absolute;
    right: 60px; top: 188px;
    text-align: right;
    font-family: "Tinos", serif;
    font-size: 18px;
    line-height: 1.3;
    color: var(--text-light);
    white-space: nowrap;
  }
  .rule {
    position: absolute;
    left: 120px; right: 60px; top: 248px;
    height: 1.5px;
    background: var(--rule);
  }
  .contacts {
    position: absolute;
    left: 125px; top: 266px;
    list-style: none;
    font-family: "Tinos", serif;
    font-size: 19px;
    color: var(--text-light);
  }
  .contacts li {
    display: flex;
    align-items: center;
    gap: 14px;
    height: 32px;
  }
  .contacts svg { width: 20px; height: 20px; fill: var(--icon-blue); flex: none; }
</style>
</head>
<body>
  <section class="card card--front" aria-label="Card front">
    <div class="brand">
      <span class="brand__dot"></span>
      <span class="brand__name">Corvana Wound Care</span>
    </div>
  </section>

  <section class="card card--back" aria-label="Card back">
    <div class="brand">
      <span class="brand__dot"></span>
      <span class="brand__name">Corvana Wound Care</span>
    </div>

    <div class="person">
      <p class="person__name">DANIEL HARGROVE</p>
      <p class="person__title">Owner</p>
    </div>

    <p class="address">421, Address line goes here<br>45452, Country name</p>

    <div class="rule"></div>

    <ul class="contacts">
      <li>
        <svg viewBox="0 0 24 24" aria-hidden="true"><path d="M6.6 10.8a15.1 15.1 0 0 0 6.6 6.6l2.2-2.2a1 1 0 0 1 1-.25 11.4 11.4 0 0 0 3.6.57 1 1 0 0 1 1 1V20a1 1 0 0 1-1 1A17 17 0 0 1 3 4a1 1 0 0 1 1-1h3.5a1 1 0 0 1 1 1c0 1.25.2 2.45.57 3.57a1 1 0 0 1-.25 1z"/></svg>
        <span>0400 555 318</span>
      </li>
      <li>
        <svg viewBox="0 0 24 24" aria-hidden="true"><path d="M2 5h20v2l-10 6L2 7zM2 9l10 6 10-6v10H2z"/></svg>
        <span>info@corvanacare.com</span>
      </li>
      <li>
        <svg viewBox="0 0 24 24" aria-hidden="true"><path d="M12 2a10 10 0 1 0 0 20 10 10 0 0 0 0-20zm-1 17.9A8 8 0 0 1 4.2 10L9 14.8v1a2 2 0 0 0 2 2zm6.9-2.5A2 2 0 0 0 16 16h-1v-3a1 1 0 0 0-1-1H8v-2h2a1 1 0 0 0 1-1V7h2a2 2 0 0 0 2-2v-.4a8 8 0 0 1 2.9 12.8z"/></svg>
        <span>www.corvanacare.com</span>
      </li>
    </ul>
  </section>
</body>
</html>
```